Business Card Design Project

Need a business card designed for a horse racing/gambling centered company.
Company name is BrightQuill.com.au
Company colours are similar to those in the logo.
Something clean and modern , designer given liberty to be creative.
Incorporate the logo is preferred.
Single or Double Sided fine
Must include :
Name
Mobile Number
Email Address
Reason: Apologies, I have been traveling unexpectedly with business and just need the extra two days to reply and give feedback before making a decision.
Industry/Entity Type
Business

```html
<!DOCTYPE html>
<html lang="en">
<head>
<meta charset="utf-8">
<title>BrightQuill.com.au Business Card</title>
<link rel="stylesheet" href="https://fonts.googleapis.com/css2?family=Open+Sans:wght@400;600;700&display=swap">
<style>
  :root {
    --backdrop: #ececec;
    --card: #ffffff;
    --card-edge: #5a5a5a;
    --brand-teal: #1f9a92;
    --ink: #4a4a4a;
    --tab-light: #6b6b6b;
    --tab-dark: #050505;
    --white: #ffffff;
  }
  * { box-sizing: border-box; margin: 0; padding: 0; }
  html, body {
    width: 1200px;
    height: 1136px;
    overflow: hidden;
    background: var(--backdrop);
    font-family: "Open Sans", Arial, sans-serif;
  }
  .canvas {
    position: relative;
    width: 1200px;
    height: 1136px;
  }
  .card {
    position: absolute;
    width: 778px;
    height: 445px;
    background: var(--card);
    border: 1px solid var(--card-edge);
  }
  .card--front { left: 64px; top: 76px; }
  .card--back { left: 310px; top: 589px; }

  .brand-mark {
    position: absolute;
    display: flex;
    align-items: center;
    justify-content: center;
    border: 8px solid var(--brand-teal);
    border-radius: 50%;
  }
  .card--front .brand-mark {
    left: 46px; top: 23px;
    width: 246px; height: 246px;
  }
  .card--back .brand-mark {
    left: 232px; top: 66px;
    width: 312px; height: 312px;
    border-width: 10px;
  }
  .brand-name {
    color: var(--brand-teal);
    font-weight: 700;
    white-space: nowrap;
  }
  .card--front .brand-name { font-size: 21px; }
  .card--back .brand-name { font-size: 27px; }

  .name-tab {
    position: absolute;
    right: 0;
    top: 70px;
    width: 256px;
    height: 92px;
    border-radius: 16px 0 0 16px;
    background: linear-gradient(90deg, var(--tab-light) 0%, #2a2a2a 45%, var(--tab-dark) 100%);
    box-shadow: 0 10px 14px -6px rgba(0,0,0,0.35);
    color: var(--white);
    text-align: center;
    padding-top: 14px;
    padding-right: 20px;
  }
  .name-tab__name { font-size: 24px; font-weight: 700; line-height: 1.2; }
  .name-tab__title { font-size: 21px; font-weight: 400; line-height: 1.2; }

  .contact-list {
    position: absolute;
    left: 46px;
    top: 290px;
    list-style: none;
    color: var(--ink);
    font-size: 19px;
  }
  .contact-list li {
    display: flex;
    align-items: center;
    height: 30px;
  }
  .contact-list svg {
    width: 16px;
    height: 16px;
    margin-right: 9px;
    fill: var(--ink);
    flex: none;
  }
  .contact-address {
    position: absolute;
    left: 46px;
    top: 392px;
    color: var(--ink);
    font-size: 19px;
  }
</style>
</head>
<body>
<main class="canvas">
  <section class="card card--front">
    <div class="brand-mark"><span class="brand-name">BrightQuill.com.au</span></div>

    <div class="name-tab">
      <div class="name-tab__name">Your Name</div>
      <div class="name-tab__title">Title</div>
    </div>

    <ul class="contact-list">
      <li>
        <svg viewBox="0 0 16 16" aria-hidden="true"><path d="M3.6 1.2l2.3 2.6-1.2 1.8c.9 2 2.6 3.7 4.6 4.6l1.8-1.2 2.6 2.3-1.5 2.4C7 13.4 2.6 9 1.3 2.7z"/></svg>
        +91 12345 67890
      </li>
      <li>
        <svg viewBox="0 0 16 16" aria-hidden="true"><path d="M4.5 1h7v14h-7zM6 3v8h4V3zm1.3 9.3v1.4h1.4v-1.4z" fill-rule="evenodd"/></svg>
        +91 12345 67890
      </li>
      <li>
        <svg viewBox="0 0 16 16" aria-hidden="true"><path d="M1.5 4h13v8.5h-13zM2 4.5l6 4.3 6-4.3" /><path d="M2 5l6 4 6-4" fill="none" stroke="#fff" stroke-width="1"/></svg>
        hello@brightquill.com.au
      </li>
    </ul>
    <p class="contact-address">Complex Name, Street Name, Area, City Name,000 000</p>
  </section>

  <section class="card card--back">
    <div class="brand-mark"><span class="brand-name">BrightQuill.com.au</span></div>
  </section>
</main>
</body>
</html>
```